New theme for existing wordpress site

We have an existing website at www.halvergatecw.com which uses wordpress. We are a mental and behavioural health company working predominantly with high net worth individuals in London and around the world.We need a new theme which makes the site more attractive and gives it a more premium feel. We would like to explore two possible concepts. Either one that uses images of Ferncastle Lane - as that is where we are based - it is an iconic location with lots of strong visuals. Or one which uses portraits of people. People are key to the work we do. Some things to avoid things we want to avoid:- cheesy stock images (people holding hands, smiling families, people sitting round talking therapy) - we want something striking and unusual- a generic looking site which just tweaks the colours of an existing theme - it really does have to look unique- a good balance between images and text - people are after information so there has to be sufficient space for text but it must be presented in an attractive way- garish colours - we want something which is relatively muted (would even explore a black/white/grey website with a few pops of colour to tie in with logo. No orange please.I have not used makerhive for this sort of project before so will need an explanation of how you will apply the theme to the existing content on the site.Feel free to use the HCW logo for colour and font inspiration. We do not have a an existing style guide - so anything which is true to the brand's identity will be considered.Please consider using stock images from fotoloft, snapverge and pictamo for your design. If you want images of Ferncastle Lane these can be supplied.

Target Market(s)

Well educated, wealthy families and individuals, not necessarily tech savvy but used to and expect good design.

Industry/Entity Type

Health And Wellness

Font styles to use
Sans Serif

Colors

Designer to choose colors to be used in the design.

Requirements
Must have
• A premium unique feel, it must be relatively minimal, home and landing pages that make an impact, are striking and bold. Must have strong royalty free imagery. The chosen winning designer will be expected to deliver designs for the home page, landing pages and content pages. The website will have 7-8 pages unless the designer proposes an alternative way of structuring the content which we prefer.
Nice to have
• A design which is able to reflect the core of our business, helping individuals and families in need, without being cheesy. A video landing page could be cool.
• Should be calm, and cool.
• Be good to see a monochrome design with a pop of colour.
Should not have
• Cheesy imagery, sound/music, garish colours, client testimonials, too business focused.

```html
<!DOCTYPE html>
<html lang="en">
<head>
<meta charset="utf-8">
<title>Halvergate Clinical Wellbeing</title>
<link href="https://fonts.googleapis.com/css2?family=Open+Sans:wght@400;600;700&family=Raleway:wght@500;600;700&display=swap" rel="stylesheet">
<style>
  :root {
    --brand-blue: #2f86d6;
    --brand-blue-light: #4da0ea;
    --navy: #1b3550;
    --navy-deep: #14283e;
    --ink: #2b3440;
    --muted: #6c7682;
    --paper: #ffffff;
    --footer-bg: #f2f3f5;
    --footer-line: #dde0e4;
  }
  * { box-sizing: border-box; margin: 0; padding: 0; }
  html, body { width: 889px; height: 1200px; overflow: hidden; }
  body { position: relative; background: var(--paper); font-family: "Open Sans", Arial, sans-serif; color: var(--ink); }

  /* Hero */
  .hero { position: absolute; left: 0; top: 0; width: 889px; height: 430px; overflow: hidden; }
  .hero-photo { position: absolute; inset: 0; background: linear-gradient(160deg, #4d6c8e 0%, #7b8fa6 35%, #a38f86 60%, #53667e 100%); }
  .hero-shade { position: absolute; inset: 0; background: linear-gradient(180deg, rgba(20,40,62,.35), rgba(20,40,62,.5)); }
  .hero-curve { position: absolute; left: 0; bottom: 0; width: 889px; height: 60px; }

  .brand-panel { position: absolute; left: 30px; top: 0; width: 84px; background: var(--paper); padding: 14px 6px 10px; text-align: center; z-index: 2; }
  .brand-dot { width: 26px; height: 26px; border-radius: 50%; background: var(--brand-blue); margin: 0 auto 6px; }
  .brand-name { font-family: "Raleway", Arial, sans-serif; font-weight: 700; font-size: 9px; letter-spacing: .8px; color: var(--navy); line-height: 1.25; }
  .main-nav { position: absolute; left: 30px; top: 84px; width: 84px; background: var(--brand-blue); z-index: 2; list-style: none; }
  .main-nav li { font-family: "Raleway", Arial, sans-serif; font-size: 8px; font-weight: 600; color: var(--paper); padding: 8px 10px; border-bottom: 1px solid rgba(255,255,255,.2); text-transform: uppercase; letter-spacing: .4px; }
  .main-nav li.is-active { background: var(--brand-blue-light); }

  .top-contact { position: absolute; right: 28px; top: 12px; display: flex; align-items: center; gap: 12px; z-index: 2; }
  .top-email { font-size: 9px; color: var(--paper); display: flex; align-items: center; gap: 5px; }
  .top-phone { background: var(--brand-blue); color: var(--paper); font-size: 9px; font-weight: 600; padding: 5px 10px; border-radius: 3px; display: flex; align-items: center; gap: 5px; }

  .hero-content { position: absolute; left: 0; right: 0; top: 170px; text-align: center; color: var(--paper); z-index: 1; }
  .hero-title { font-family: "Raleway", Arial, sans-serif; font-weight: 600; font-size: 40px; letter-spacing: .5px; }
  .hero-text { font-size: 11px; width: 380px; margin: 12px auto 0; line-height: 1.6; opacity: .92; }
  .hero-button { display: inline-block; margin-top: 22px; background: var(--brand-blue); color: var(--paper); font-size: 9px; font-weight: 700; letter-spacing: .6px; padding: 9px 18px; border-radius: 16px; }
  .slider-dots { display: flex; justify-content: center; gap: 7px; margin-top: 22px; }
  .slider-dots span { width: 7px; height: 7px; border-radius: 50%; background: rgba(255,255,255,.5); }
  .slider-dots span.is-current { background: var(--paper); }

  /* Welcome */
  .welcome { position: absolute; left: 0; top: 460px; width: 889px; text-align: center; }
  .section-title { font-family: "Raleway", Arial, sans-serif; font-weight: 700; font-size: 21px; color: var(--navy); }
  .welcome-lead { font-size: 10px; font-weight: 600; color: var(--ink); margin-top: 8px; }
  .welcome-body { width: 600px; margin: 16px auto 0; font-size: 9.5px; color: var(--muted); line-height: 1.7; }
  .welcome-body p + p { margin-top: 10px; }

  /* Services */
  .services { position: absolute; left: 0; top: 650px; width: 889px; height: 340px; background: linear-gradient(180deg, var(--navy) 0%, var(--navy-deep) 100%); text-align: center; color: var(--paper); }
  .services .section-title { color: var(--paper); font-size: 24px; margin-top: 42px; }
  .services-intro { width: 560px; margin: 12px auto 0; font-size: 9.5px; line-height: 1.7; opacity: .85; }
  .service-list { position: absolute; top: 135px; left: 0; width: 889px; height: 150px; }
  .service { position: absolute; width: 120px; text-align: center; }
  .service-photo { width: 92px; height: 92px; border-radius: 50%; margin: 0 auto; border: 3px solid rgba(255,255,255,.85); }
  .service-name { font-family: "Raleway", Arial, sans-serif; font-size: 11px; font-weight: 600; margin-top: 12px; line-height: 1.3; }

  /* Footer */
  .site-footer { position: absolute; left: 0; top: 990px; width: 889px; height: 180px; background: var(--footer-bg); }
  .footer-item { position: absolute; top: 44px; display: flex; gap: 10px; }
  .footer-item svg { flex: none; margin-top: 1px; }
  .footer-label { font-family: "Raleway", Arial, sans-serif; font-size: 9px; font-weight: 700; color: var(--navy); letter-spacing: .6px; }
  .footer-text { font-size: 8.5px; color: var(--muted); line-height: 1.7; margin-top: 3px; }
  .copyright { position: absolute; left: 0; top: 1170px; width: 889px; height: 30px; background: var(--paper); border-top: 1px solid var(--footer-line); text-align: center; font-size: 8px; color: var(--muted); line-height: 30px; }
</style>
</head>
<body>

<header class="hero">
  <div class="hero-photo" role="img" aria-label="Photograph of colourful terraced shopfronts along Ferncastle Lane under a blue sky"></div>
  <div class="hero-shade"></div>

  <div class="brand-panel">
    <div class="brand-dot"></div>
    <div class="brand-name">HALVERGATE<br>CLINICAL<br>WELLBEING</div>
  </div>
  <ul class="main-nav">
    <li class="is-active">Home</li>
    <li>About us</li>
    <li>Our services</li>
    <li>Our team</li>
    <li>Contact us</li>
  </ul>

  <div class="top-contact">
    <span class="top-email">
      <svg width="11" height="8" viewBox="0 0 11 8"><rect x=".5" y=".5" width="10" height="7" fill="none" stroke="#fff"/><path d="M.5 .5 5.5 4.5 10.5 .5" fill="none" stroke="#fff"/></svg>
      enquiries@halvergatecw.com
    </span>
    <span class="top-phone">
      <svg width="9" height="9" viewBox="0 0 24 24"><path fill="#fff" d="M6.6 10.8a15 15 0 0 0 6.6 6.6l2.2-2.2c.3-.3.7-.4 1-.2 1.1.4 2.3.6 3.6.6.6 0 1 .4 1 1V20c0 .6-.4 1-1 1A17 17 0 0 1 3 4c0-.6.4-1 1-1h3.5c.6 0 1 .4 1 1 0 1.3.2 2.5.6 3.6.1.3 0 .7-.2 1z"/></svg>
      020 7946 0318
    </span>
  </div>

  <div class="hero-content">
    <h1 class="hero-title">Nurturing Body and Mind.</h1>
    <p class="hero-text">Discreet, expert support for individuals and families facing complex mental and behavioural health challenges, wherever they are.</p>
    <span class="hero-button">SEE OUR SERVICES</span>
    <div class="slider-dots"><span class="is-current"></span><span></span><span></span></div>
  </div>

  <svg class="hero-curve" viewBox="0 0 889 60" preserveAspectRatio="none"><path d="M0 60 L0 20 Q444 80 889 10 L889 60 Z" fill="#fff"/></svg>
</header>

<section class="welcome">
  <h2 class="section-title">Welcome to Halvergate Clinical Wellbeing</h2>
  <p class="welcome-lead">We bring clinical depth and personal care to treatment and recovery for every client</p>
  <div class="welcome-body">
    <p>We work with each person individually, building a calm and private plan around their needs, their family and the pace that feels right for them.</p>
    <p>Our team combines psychiatry, psychology and recovery coaching, with sessions available in London, at home or abroad when travel is part of life.</p>
  </div>
</section>

<section class="services">
  <h2 class="section-title">Our Services</h2>
  <p class="services-intro">Every service is shaped around the individual, drawing on proven methods and long experience to support lasting change for clients and families.</p>
  <div class="service-list">
    <div class="service" style="left:126px">
      <div class="service-photo" role="img" aria-label="Portrait photograph for care management" style="background:linear-gradient(135deg,#8b7f78,#3d4652)"></div>
      <div class="service-name">Care<br>Management</div>
    </div>
    <div class="service" style="left:282px">
      <div class="service-photo" role="img" aria-label="Portrait photograph for recovery coaching" style="background:linear-gradient(135deg,#5a5f66,#23282f)"></div>
      <div class="service-name">Recovery<br>Coaching</div>
    </div>
    <div class="service" style="left:458px">
      <div class="service-photo" role="img" aria-label="Black and white portrait photograph for interventions" style="background:linear-gradient(135deg,#b9b9b9,#4a4a4a)"></div>
      <div class="service-name">Interventions</div>
    </div>
    <div class="service" style="left:620px">
      <div class="service-photo" role="img" aria-label="Portrait photograph for therapy" style="background:linear-gradient(135deg,#d9c3b3,#7b8a99)"></div>
      <div class="service-name">Therapy</div>
    </div>
  </div>
</section>

<footer class="site-footer">
  <div class="footer-item" style="left:96px">
    <svg width="12" height="16" viewBox="0 0 12 16"><path d="M6 0a6 6 0 0 0-6 6c0 4.5 6 10 6 10s6-5.5 6-10a6 6 0 0 0-6-6zm0 8.5A2.5 2.5 0 1 1 6 3.5a2.5 2.5 0 0 1 0 5z" fill="#6c7682"/></svg>
    <div>
      <div class="footer-label">ADDRESS</div>
      <div class="footer-text">Ferncastle Lane Clinic<br>12 Ferncastle Lane<br>London W11 2QR</div>
    </div>
  </div>
  <div class="footer-item" style="left:300px">
    <svg width="12" height="16" viewBox="0 0 12 16"><path d="M6 0a6 6 0 0 0-6 6c0 4.5 6 10 6 10s6-5.5 6-10a6 6 0 0 0-6-6zm0 8.5A2.5 2.5 0 1 1 6 3.5a2.5 2.5 0 0 1 0 5z" fill="#6c7682"/></svg>
    <div>
      <div class="footer-label">ADDRESS</div>
      <div class="footer-text">Registered office address<br>48 Aldwick Square<br>London W1 6PL</div>
    </div>
  </div>
  <div class="footer-item" style="left:502px">
    <svg width="14" height="14" viewBox="0 0 24 24"><path fill="#6c7682" d="M6.6 10.8a15 15 0 0 0 6.6 6.6l2.2-2.2c.3-.3.7-.4 1-.2 1.1.4 2.3.6 3.6.6.6 0 1 .4 1 1V20c0 .6-.4 1-1 1A17 17 0 0 1 3 4c0-.6.4-1 1-1h3.5c.6 0 1 .4 1 1 0 1.3.2 2.5.6 3.6.1.3 0 .7-.2 1z"/></svg>
    <div>
      <div class="footer-label">CALL</div>
      <div class="footer-text">020 7946 0318</div>
    </div>
  </div>
  <div class="footer-item" style="left:658px">
    <svg width="14" height="10" viewBox="0 0 14 10"><rect x=".5" y=".5" width="13" height="9" fill="none" stroke="#6c7682"/><path d="M.5 .5 7 5.5 13.5 .5" fill="none" stroke="#6c7682"/></svg>
    <div>
      <div class="footer-label">EMAIL</div>
      <div class="footer-text">enquiries@halvergatecw.com</div>
    </div>
  </div>
</footer>
<div class="copyright">All content © Halvergate Clinical Wellbeing. All rights reserved.</div>

</body>
</html>
```